New National Dermatology Group needs a business card!

We need a business card for our new national company that has 3 brands within the business:
Brellow Dermal Care, Tamvirk Dermal Care and Orvandel Dermal Care.
We help people access dermatology services close to home throughout Australia.
We need a business card that has:
all 3 logos on it,
Our websites (there are three, listed above)
Our email (there are three, listed above)
The location of our first clinic: 41 Wendle St Harlowe Park (this can then be changed for each location as required)

```html
<!DOCTYPE html>
<html lang="en">
<head>
<meta charset="utf-8">
<title>Brellow, Tamvirk and Orvandel Dermal Care – Business Card</title>
<link href="https://fonts.googleapis.com/css2?family=Poppins:wght@400;500;700&display=swap" rel="stylesheet">
<style>
  :root {
    --stage: #565656;
    --paper: #ffffff;
    --ink: #1a1a1a;
    --green: #22ad4c;
    --orange: #f28227;
    --brown: #7a3e1d;
    --divider: #c9c9c9;
  }
  * { margin: 0; padding: 0; box-sizing: border-box; }
  html, body { width: 1200px; height: 1200px; overflow: hidden; }
  body { background: var(--stage); font-family: "Poppins", sans-serif; color: var(--ink); position: relative; }

  .card { position: absolute; left: 263px; width: 673px; height: 385px; background: var(--paper); overflow: hidden; }
  .card--front { top: 189px; }
  .card--back { top: 625px; }

  /* Front */
  .column { position: absolute; top: 0; width: 217px; height: 338px; text-align: center; }
  .column--brellow { left: 12px; color: var(--green); }
  .column--tamvirk { left: 229px; color: var(--orange); }
  .column--orvandel { left: 446px; color: var(--brown); }
  .divider { position: absolute; top: 42px; width: 1px; height: 252px; background: var(--divider); }
  .divider--one { left: 228px; }
  .divider--two { left: 445px; }

  .brand-name { position: absolute; left: 0; right: 0; top: 36px; font-weight: 500; line-height: 1; text-transform: uppercase; }
  .brand-name .word { display: block; font-size: 31px; letter-spacing: 1.5px; }
  .brand-name .sub { display: block; font-size: 10px; letter-spacing: 4.5px; margin-top: 4px; }

  .icon { position: absolute; left: 50%; width: 37px; height: 37px; margin-left: -18.5px; }
  .icon--pin { top: 108px; }
  .icon--mail { top: 205px; }

  .detail { position: absolute; left: 0; right: 0; font-size: 15px; line-height: 19px; color: var(--ink); }
  .detail--address { top: 151px; }
  .detail--email { top: 247px; }
  .website { position: absolute; left: 0; right: 0; top: 284px; font-size: 15.5px; font-weight: 700; }

  .band { position: absolute; left: 0; width: 100%; }
  .band--green { top: 338px; height: 14px; background: var(--green); }
  .band--orange { top: 352px; height: 16px; background: var(--orange); }
  .band--brown { top: 368px; height: 17px; background: var(--brown); }

  /* Back */
  .back-shapes { position: absolute; inset: 0; width: 673px; height: 385px; }
  .back-logo { position: absolute; left: 55px; width: 240px; text-align: center; font-weight: 500; text-transform: uppercase; line-height: 1; }
  .back-logo .word { display: block; font-size: 38px; letter-spacing: 1.5px; }
  .back-logo .sub { display: block; font-size: 12px; letter-spacing: 5.5px; margin-top: 6px; }
  .back-logo--brellow { top: 52px; color: var(--green); }
  .back-logo--tamvirk { top: 143px; color: var(--orange); }
  .back-logo--orvandel { top: 234px; color: var(--brown); }
</style>
</head>
<body>

<section class="card card--front">
  <div class="divider divider--one"></div>
  <div class="divider divider--two"></div>

  <div class="column column--brellow">
    <p class="brand-name"><span class="word">Brellow</span><span class="sub">Dermal Care</span></p>
    <svg class="icon icon--pin" viewBox="0 0 37 37" fill="none" stroke="currentColor" stroke-width="1.3"><circle cx="18.5" cy="18.5" r="17.5"/><path d="M18.5 28c-4-5-6.5-8.5-6.5-11.5a6.5 6.5 0 0 1 13 0c0 3-2.5 6.5-6.5 11.5z"/><circle cx="18.5" cy="16.3" r="2.4"/></svg>
    <p class="detail detail--address">41 Wendle St<br>Harlowe Park</p>
    <svg class="icon icon--mail" viewBox="0 0 37 37" fill="none" stroke="currentColor" stroke-width="1.3"><circle cx="18.5" cy="18.5" r="17.5"/><rect x="11" y="13.5" width="15" height="10"/><path d="M11 13.5l7.5 6 7.5-6M11 23.5l5.5-5M26 23.5l-5.5-5"/></svg>
    <p class="detail detail--email">brellow@clinicmail.com</p>
    <p class="website">brellowclinic.com</p>
  </div>

  <div class="column column--tamvirk">
    <p class="brand-name"><span class="word">Tamvirk</span><span class="sub">Dermal Care</span></p>
    <svg class="icon icon--pin" viewBox="0 0 37 37" fill="none" stroke="currentColor" stroke-width="1.3"><circle cx="18.5" cy="18.5" r="17.5"/><path d="M18.5 28c-4-5-6.5-8.5-6.5-11.5a6.5 6.5 0 0 1 13 0c0 3-2.5 6.5-6.5 11.5z"/><circle cx="18.5" cy="16.3" r="2.4"/></svg>
    <p class="detail detail--address">Address of clinic</p>
    <svg class="icon icon--mail" viewBox="0 0 37 37" fill="none" stroke="currentColor" stroke-width="1.3"><circle cx="18.5" cy="18.5" r="17.5"/><rect x="11" y="13.5" width="15" height="10"/><path d="M11 13.5l7.5 6 7.5-6M11 23.5l5.5-5M26 23.5l-5.5-5"/></svg>
    <p class="detail detail--email">tamvirk@clinicmail.com</p>
    <p class="website">tamvirkclinic.com</p>
  </div>

  <div class="column column--orvandel">
    <p class="brand-name"><span class="word">Orvandel</span><span class="sub">Dermal Care</span></p>
    <svg class="icon icon--pin" viewBox="0 0 37 37" fill="none" stroke="currentColor" stroke-width="1.3"><circle cx="18.5" cy="18.5" r="17.5"/><path d="M18.5 28c-4-5-6.5-8.5-6.5-11.5a6.5 6.5 0 0 1 13 0c0 3-2.5 6.5-6.5 11.5z"/><circle cx="18.5" cy="16.3" r="2.4"/></svg>
    <p class="detail detail--address">Address of clinic</p>
    <svg class="icon icon--mail" viewBox="0 0 37 37" fill="none" stroke="currentColor" stroke-width="1.3"><circle cx="18.5" cy="18.5" r="17.5"/><rect x="11" y="13.5" width="15" height="10"/><path d="M11 13.5l7.5 6 7.5-6M11 23.5l5.5-5M26 23.5l-5.5-5"/></svg>
    <p class="detail detail--email">orvandel@clinicmail.com</p>
    <p class="website">orvandelclinic.com</p>
  </div>

  <div class="band band--green"></div>
  <div class="band band--orange"></div>
  <div class="band band--brown"></div>
</section>

<section class="card card--back">
  <svg class="back-shapes" viewBox="0 0 673 385">
    <polygon fill="var(--green)" points="466,0 575,0 401,351 0,351 0,338 299,338"/>
    <polygon fill="var(--orange)" points="575,0 673,0 673,25 504,368 0,368 0,351 401,351"/>
    <polygon fill="var(--brown)" points="673,25 673,385 0,385 0,368 504,368"/>
  </svg>
  <p class="back-logo back-logo--brellow"><span class="word">Brellow</span><span class="sub">Dermal Care</span></p>
  <p class="back-logo back-logo--tamvirk"><span class="word">Tamvirk</span><span class="sub">Dermal Care</span></p>
  <p class="back-logo back-logo--orvandel"><span class="word">Orvandel</span><span class="sub">Dermal Care</span></p>
</section>

</body>
</html>
```